Bref créative
Marketing Materials For Brightwater Home Renovations, LLC
Need brochure, postcards, Thank you/referral cards, Truck sign, T-shirt
Long Island Home Remodeling & Design
Looking for a brochure design for racks. A thank you note that can also serve as a referral card. I will post the referral content in the comment section. The truck sign will be a magnet approx. 24" x 24". Flexible with the t-shirt.
Construction
I'm looking for professional as well as heartfelt. We are a home remodeling and design company focused on customer service, quality, value and creativity. Target audience is people looking for more than a faceless general contractor to remodel their home. We are striving to be a home improvement company with personality and enthusiasm.
not sure besides basic info. You can take a look at our website in progress for ideas of who we are and aim to be. Brightwaterhomerenovations.example As long as I can edit the content in the end, I'm ok with you putting in filler for now.
Brightwater Home Renovations, LLC Logo
Mug Shot
Some Literature
referral content

```html
<!DOCTYPE html>
<html lang="en">
<head>
<meta charset="utf-8">
<title>Brightwater Home Renovations – Trifold Brochure</title>
<link href="https://fonts.googleapis.com/css2?family=Open+Sans:wght@400;600;700;800&display=swap" rel="stylesheet">
<style>
  :root{
    --page:#ffffff;
    --navy:#123a66;
    --blue-deep:#1e64a8;
    --blue:#2f86c8;
    --blue-light:#8cc4ec;
    --ink:#3b3b3b;
    --ink-soft:#5a5a5a;
    --accent:#1f78c2;
    --rule:#d7dde3;
  }
  *{box-sizing:border-box;margin:0;padding:0}
  html,body{width:1200px;height:935px;overflow:hidden;background:var(--page)}
  body{font-family:"Open Sans",Arial,sans-serif;position:relative}
  .brochure{position:absolute;left:47px;top:22px;width:1113px;height:893px;box-shadow:0 2px 8px rgba(0,0,0,.25);background:#fff;overflow:hidden}
  .panel{position:absolute;top:0;height:100%}
  .panel--about{left:0;width:390px;background:linear-gradient(180deg,var(--blue-deep) 0%,var(--blue) 45%,var(--blue-light) 100%)}
  .panel--services{left:390px;width:356px;background:linear-gradient(180deg,#f4f6f8 0%,#ffffff 40%)}
  .panel--process{left:746px;width:367px;background:linear-gradient(180deg,#eef2f5 0%,#ffffff 35%)}

  .panel-header{position:absolute;top:58px;height:38px;background:var(--navy);display:flex;align-items:center;gap:10px;padding-left:24px;color:#fff;font-weight:700;font-size:17px;white-space:nowrap}
  .panel--about .panel-header{left:22px;width:168px}
  .panel--services .panel-header{left:0;width:215px;background:linear-gradient(90deg,var(--navy),#2c5c8c)}
  .panel--process .panel-header{left:0;width:175px;background:linear-gradient(90deg,var(--navy),#2c5c8c)}
  .header-icon{width:22px;height:22px;flex:none}

  .about-copy{position:absolute;left:24px;top:112px;width:330px;color:#fff;font-size:11.6px;line-height:1.38}
  .about-copy p{margin-bottom:13px}
  .about-copy p.narrow{width:178px}
  .workers-photo{position:absolute;left:205px;top:462px;width:175px;height:420px;border-radius:70px 70px 0 0;background:linear-gradient(180deg,#e6e6e6 0%,#d4883c 45%,#8a8e96 100%);opacity:.95}

  .service-list{position:absolute;left:42px;list-style:none;font-weight:700;font-size:18px;line-height:1.42;color:var(--ink);letter-spacing:.3px}
  .service-list li{display:flex;align-items:center;gap:7px}
  .service-list li::before{content:"";width:7px;height:7px;background:var(--accent);flex:none}
  .service-list--top{top:114px}
  .service-list--bottom{top:628px}
  .blueprint-wash{position:absolute;right:0;top:0;width:170px;height:330px;background:linear-gradient(135deg,rgba(200,215,230,0) 0%,rgba(190,205,220,.55) 100%)}

  .collage{position:absolute;left:390px;top:338px;width:723px;height:272px}

  .process-block{position:absolute;color:var(--ink-soft);font-size:11px;line-height:1.36}
  .process-block h3{color:var(--accent);font-size:12px;font-weight:700;margin-bottom:1px}
  .process-block p{margin-bottom:9px}
  .process-top{left:22px;top:108px;width:330px}
  .process-bottom{left:150px;top:628px;width:205px}
  .tools-wash{position:absolute;left:0;top:622px;width:150px;height:271px;background:linear-gradient(160deg,rgba(210,205,190,.6) 0%,rgba(255,255,255,0) 100%)}
  .fold{position:absolute;top:0;width:1px;height:100%;background:var(--rule)}
</style>
</head>
<body>
<main class="brochure">

  <section class="panel panel--about">
    <h2 class="panel-header">
      <svg class="header-icon" viewBox="0 0 22 22"><circle cx="11" cy="11" r="10" fill="#4aa3e0"/><path d="M5 11.5 11 6l6 5.5M7 10.5V16h8v-5.5" fill="none" stroke="#fff" stroke-width="1.6"/></svg>
      About Us
    </h2>
    <div class="about-copy">
      <p>Brightwater Home Renovations, LLC is a Long Island family owned &amp; operated business spanning three generations of knowledge and handiwork. Beginning with masonry, to home exterior &amp; finally expanding to interior remodeling &amp; design, Brightwater Home Renovations can service all of your home remodeling needs.</p>
      <p>We are a relatively small company. We provide an intimate service the entire length of the job, from concept &amp; design to the final inspection. There will be no nameless faces walking around your house. You will know and like each one of us. We are professional, courteous &amp; hardworking. Being a boutique company helps to keep your cost down as well as keeping your job a priority from beginning to end. We guarantee all our work, with follow-up visits and/or phone calls, your choice, to provide you with customer service beyond completion of your job.</p>
      <p class="narrow">Creativity and enthusiasm is something that we pride ourselves on. We feel this is what separates us from other remodeling services. We understand that other successful contractors can provide you with great service, as it should be, and we respect each one of our peers in the industry that do just that. But at Brightwater Home Renovations, we feel we will take a step further offering you the excitement and enthusiasm that your home remodeling project deserves. As the old saying goes, "Service with a smile."</p>
    </div>
    <div class="workers-photo" role="img" aria-label="Photo of two smiling contractors in work overalls holding tools"></div>
  </section>

  <section class="panel panel--services">
    <div class="blueprint-wash" role="img" aria-label="Faint background photo of house blueprints"></div>
    <h2 class="panel-header">
      <svg class="header-icon" viewBox="0 0 22 22"><circle cx="11" cy="11" r="10" fill="#4aa3e0"/><path d="M6 16l6-6M12 10l2-4 3 3-4 2" fill="none" stroke="#fff" stroke-width="1.6"/></svg>
      Services Provided
    </h2>
    <ul class="service-list service-list--top">
      <li>ROOFING</li><li>SIDING</li><li>GUTTERS</li><li>WINDOWS</li><li>DOORS</li><li>KITCHENS</li><li>BATHS</li><li>BASEMENTS</li>
    </ul>
    <ul class="service-list service-list--bottom">
      <li>FLOORS</li><li>MOLDINGS</li><li>DECKS</li><li>SHEDS</li><li>REMODELS</li><li>DESIGN</li><li>HANDYMAN</li>
    </ul>
  </section>

  <section class="panel panel--process">
    <h2 class="panel-header">
      <svg class="header-icon" viewBox="0 0 22 22"><circle cx="11" cy="11" r="10" fill="#4aa3e0"/><path d="M6 11.5l3.5 3.5L16 8" fill="none" stroke="#fff" stroke-width="1.8"/></svg>
      Our Process
    </h2>
    <div class="process-block process-top">
      <h3>FREE Estimates <span style="font-weight:400">and</span> In-Home Consultation.</h3>
      <p>We will talk about your project and provide you with a detailed estimate encompassing the entire scope of the job. Timing, cost, etc.</p>
      <h3>Design</h3>
      <p>From concept to design, we will work together to explore a variety of options to make sure your remodel projects fits YOUR needs. Each project is unique to the individual, as is price range. We understand this and look forward to planning a project both creative and economical.</p>
    </div>
    <div class="tools-wash" role="img" aria-label="Faded photo of measuring tools on plans"></div>
    <div class="process-block process-bottom">
      <h3>Work</h3>
      <p>From start to finish, we will be on time and maintain steady progress, building to your exact specifications.</p>
      <h3>Inspect</h3>
      <p>We thoroughly inspect every aspect of our work performed making sure it matches your specifications and exceeds your expectations.</p>
      <h3>Completion</h3>
      <p>As we finish our job, on time and within budget, you will start enjoying, feeling comforted in our %100 customer satisfaction guarantee.</p>
    </div>
  </section>

  <svg class="collage" viewBox="0 0 723 272" role="img" aria-label="Diagonal collage of photos: wood framing, tools, a house model, a kitchen and paint swatches">
    <defs>
      <linearGradient id="wood" x1="0" y1="0" x2="1" y2="1"><stop offset="0" stop-color="#d9b384"/><stop offset="1" stop-color="#8b5a2b"/></linearGradient>
      <linearGradient id="house" x1="0" y1="0" x2="1" y2="1"><stop offset="0" stop-color="#b7c9d8"/><stop offset="1" stop-color="#6e7d86"/></linearGradient>
      <linearGradient id="kitchen" x1="0" y1="0" x2="1" y2="1"><stop offset="0" stop-color="#c9a27a"/><stop offset="1" stop-color="#5e4331"/></linearGradient>
      <linearGradient id="paint" x1="0" y1="0" x2="1" y2="0"><stop offset="0" stop-color="#e0463a"/><stop offset=".35" stop-color="#f2c230"/><stop offset=".7" stop-color="#4aa0d8"/><stop offset="1" stop-color="#5bb36a"/></linearGradient>
    </defs>
    <polygon points="0,70 356,0 356,272 0,272" fill="url(#wood)"/>
    <polygon points="0,190 200,150 356,272 0,272" fill="#7a5a3c" opacity=".55"/>
    <polygon points="356,0 520,0 470,160 356,185" fill="url(#house)"/>
    <polygon points="520,0 723,0 723,105 470,160" fill="url(#kitchen)"/>
    <polygon points="356,185 470,160 723,105 723,272 356,272" fill="url(#paint)" opacity=".9"/>
    <line x1="356" y1="0" x2="356" y2="272" stroke="#fff" stroke-width="3"/>
    <line x1="470" y1="160" x2="520" y2="0" stroke="#fff" stroke-width="3"/>
    <line x1="356" y1="185" x2="723" y2="105" stroke="#fff" stroke-width="3"/>
  </svg>

  <span class="fold" style="left:390px"></span>
  <span class="fold" style="left:746px"></span>
</main>
</body>
</html>
```